Brightwater Commerce Business Card Design

Hello,

Attached you will find our logo. We are looking for a sharp business card design.

Other info to be included is:
Name: Marcus Delaney
Title: CEO
Office: (555) 382-7146
Cell: (555) 382-7146
E-mail address: marcus@brightwatercommerce.example
website: www.BrightwaterCommerce.example

```html
<!DOCTYPE html>
<html lang="en">
<head>
<meta charset="utf-8">
<title>Brightwater Commerce – Business Card</title>
<link rel="stylesheet" href="https://fonts.googleapis.com/css2?family=Montserrat:wght@300;400;700&display=swap">
<style>
  :root {
    --backdrop: #d9d9d9;
    --card-white: #ffffff;
    --brand-red: #e4353f;
    --brand-blue: #2466b8;
    --ink-blue: #2a64b0;
    --text-light: #ffffff;
    --title-pink: #ffd3d6;
  }
  * { box-sizing: border-box; margin: 0; padding: 0; }
  html, body {
    width: 1200px; height: 1000px; overflow: hidden;
    background: var(--backdrop);
    font-family: "Montserrat", sans-serif;
  }
  .canvas {
    width: 1200px; height: 1000px;
    display: flex; align-items: center; justify-content: center;
  }
  .business-card {
    position: relative;
    width: 900px; height: 514px;
    background: var(--card-white);
    box-shadow: 0 10px 30px rgba(0,0,0,0.18);
    overflow: hidden;
  }
  .brand {
    position: absolute; top: 0; left: 0; right: 0; height: 190px;
    display: flex; align-items: center; justify-content: center; gap: 14px;
    padding-top: 30px;
  }
  .brand-dot {
    width: 26px; height: 26px; border-radius: 50%;
    background: var(--brand-blue);
  }
  .brand-name {
    font-weight: 700; font-size: 30px; letter-spacing: 1px;
    color: var(--ink-blue); text-transform: uppercase;
  }
  .name-band {
    position: absolute; top: 190px; left: 0; right: 0; height: 140px;
    background: var(--brand-red);
    display: flex; flex-direction: column; align-items: center; justify-content: center;
    color: var(--text-light);
  }
  .person-name {
    font-weight: 700; font-size: 44px; letter-spacing: 1px; text-transform: uppercase;
    line-height: 1.1;
  }
  .person-title {
    font-weight: 300; font-size: 30px; color: var(--title-pink); line-height: 1.2;
  }
  .contact-band {
    position: absolute; top: 330px; left: 0; right: 0; height: 150px;
    background: var(--brand-blue);
    display: grid; grid-template-columns: 1fr 1fr;
    padding: 32px 40px 0 110px; row-gap: 22px; column-gap: 30px;
    color: var(--text-light);
  }
  .contact-column { display: flex; flex-direction: column; gap: 24px; }
  .contact-item {
    display: flex; align-items: center; gap: 16px;
    font-weight: 300; font-size: 19px; white-space: nowrap;
  }
  .contact-item.is-small { font-size: 15px; }
  .contact-icon { width: 22px; height: 22px; flex: none; fill: var(--text-light); }
  .contact-icon.is-outline { fill: none; stroke: var(--text-light); stroke-width: 1.6; }
</style>
</head>
<body>
<main class="canvas">
  <article class="business-card">
    <header class="brand">
      <span class="brand-dot"></span>
      <span class="brand-name">Brightwater Commerce</span>
    </header>

    <section class="name-band">
      <h1 class="person-name">Marcus Delaney</h1>
      <p class="person-title">Chief Executive Officer</p>
    </section>

    <section class="contact-band">
      <div class="contact-column">
        <div class="contact-item">
          <svg class="contact-icon" viewBox="0 0 24 24" aria-hidden="true"><path d="M12 3 2 12h3v9h5v-6h4v6h5v-9h3z"/></svg>
          <span>(555) 382-7146</span>
        </div>
        <div class="contact-item is-small">
          <svg class="contact-icon" viewBox="0 0 24 24" aria-hidden="true"><path d="M2 5h20v14H2z M3 6l9 7 9-7" fill="none" stroke="#fff" stroke-width="1.8"/></svg>
          <span>marcus@brightwatercommerce.example</span>
        </div>
      </div>
      <div class="contact-column">
        <div class="contact-item">
          <svg class="contact-icon" viewBox="0 0 24 24" aria-hidden="true"><path d="M6.6 10.8a15 15 0 0 0 6.6 6.6l2.2-2.2a1 1 0 0 1 1-.25 11.4 11.4 0 0 0 3.6.6 1 1 0 0 1 1 1V20a1 1 0 0 1-1 1A17 17 0 0 1 3 4a1 1 0 0 1 1-1h3.5a1 1 0 0 1 1 1 11.4 11.4 0 0 0 .6 3.6 1 1 0 0 1-.25 1z"/></svg>
          <span>(555) 382-7146</span>
        </div>
        <div class="contact-item is-small">
          <svg class="contact-icon is-outline" viewBox="0 0 24 24" aria-hidden="true"><circle cx="12" cy="12" r="9.5"/><ellipse cx="12" cy="12" rx="4" ry="9.5"/><path d="M2.5 12h19M4 7h16M4 17h16"/></svg>
          <span>www.BrightwaterCommerce.example</span>
        </div>
      </div>
    </section>
  </article>
</main>
</body>
</html>
```